business card design - photography

I am a fine art photographer. I would like to approach galleries to exhibit my work and need a business card.

The card should convey creativity and simplicity.
I would like a double sided card.

Some options:
1. An all white card with raised or embossed text or design to create a tactile finish.
2. a white and dark grey design would also work well.
3. Would be great to use my name as part of the design but not essential.
4. My name and title on the front, other details on the back of card.

The final design should be simple, minimal, elegant and innovative.
Being minimal, it will be more about texture, text size and placement.

examples of designs I would prefer provided here:
http://layoutmuse.net/ideas/40-plain-and-graceful-calling-card-layouts

I'm also open to other designs that may be unusual and unique.

Love this:
http://www.snapvault.com/pics/morningverses/583017264
Updates

I have uploaded a psd file after playing around in photoshop with various fonts.  I like the font (which I downloaded from typeshelf.net called Arual) but the design probably needs some refining.  I hope this helps.  If you'd like me to change the format of the file, please let me know.

Marta

Target Market(s)

Art Gallery owners/administrators and customers.

Industry/Entity Type

Business

Requirements
Must have
• A unique look.

Matte, silky finish or heavy textured stock. Double-sided card.

Front:
my name
photography by

Back:
phone no
email
web address
Nice to have
• Letterpress
embrossed
Clean fonts
Should not have
• Do not use illustrations of cameras or lenses.
No frames around the card edge.

```html
<!DOCTYPE html>
<html lang="en">
<head>
<meta charset="UTF-8">
<title>Marta Halvey – Photography</title>
<link rel="stylesheet" href="https://fonts.googleapis.com/css2?family=Arimo:wght@400;700&display=swap">
<style>
  :root {
    --card-orange: #ff9c00;
    --ink-grey: #4a4a4a;
    --emboss-light: rgba(255, 214, 140, 0.55);
    --emboss-dark: rgba(60, 30, 0, 0.45);
  }

  html, body {
    margin: 0;
    padding: 0;
    width: 1200px;
    height: 734px;
    overflow: hidden;
  }

  .card-front {
    position: relative;
    width: 1200px;
    height: 734px;
    background: var(--card-orange);
  }

  .signature-line {
    position: absolute;
    right: 48px;
    bottom: 22px;
    margin: 0;
    font-family: "Arimo", "Helvetica Neue", Arial, sans-serif;
    font-size: 58px;
    line-height: 1;
    letter-spacing: 0.2px;
    color: var(--ink-grey);
    white-space: nowrap;
    text-shadow:
      0 2px 1px var(--emboss-light),
      0 -1px 1px var(--emboss-dark);
  }

  .signature-line .title {
    font-weight: 700;
  }

  .signature-line .name {
    font-weight: 400;
  }
</style>
</head>
<body>
  <main class="card-front">
    <p class="signature-line">
      <span class="title">Photography by</span>
      <span class="name">Marta Halvey</span>
    </p>
  </main>
</body>
</html>
```